Powerpoint Presentation design template

I am looking for a PPT presentation that show class and professionalism and in the same colour them as the logo. It should be simple, but yet classy and pro. The business is an oil and gas exploration and exploitation business. The business has nothing to do with solar panel and other renewable energies, so please no solar panel or wind farms in the background. It would be more oil rigs and LNG plant in the background of some slide templates...

oil and gas exploration and exploitation

```html
<!DOCTYPE html>
<html lang="en">
<head>
<meta charset="utf-8">
<title>Kestrel Energy – Oil &amp; Gas Presentation Template</title>
<link rel="stylesheet" href="https://fonts.googleapis.com/css2?family=Poppins:ital,wght@0,300;0,400;0,500;0,600;0,700;1,600;1,700&display=swap">
<style>
  :root{
    --board:#a6a6a6;
    --paper:#f3f3f3;
    --blue:#0d8fd6;
    --sky:#5bbfe6;
    --royal:#3a7fd5;
    --navy:#1d4e8f;
    --green:#6cc04a;
    --teal:#3bb08f;
    --ink:#222;
    --pill:#e6e8f2;
  }
  *{box-sizing:border-box;margin:0;padding:0}
  html,body{width:1200px;height:848px;overflow:hidden;background:var(--board)}
  body{font-family:"Poppins",sans-serif;color:var(--ink);position:relative}
  .frame{position:absolute;width:calc(800px * var(--s));height:calc(450px * var(--s));overflow:hidden}
  .frame.raised{box-shadow:0 1px 3px rgba(0,0,0,.35)}
  .slide{position:absolute;left:0;top:0;width:800px;height:450px;background:var(--paper);transform:scale(var(--s));transform-origin:0 0;overflow:hidden}
  .waves{position:absolute;inset:0;width:800px;height:450px}
  .abs{position:absolute}
  .photo{position:absolute;overflow:hidden}
  .photo.round{border-radius:50%;border:6px solid var(--green)}
  .title{font-weight:700;color:var(--blue);line-height:1.15;text-transform:uppercase}
  .body-text{font-size:12px;line-height:1.45;color:var(--ink)}
  .white{color:#fff}
  /* cover */
  .cover-title{left:430px;top:145px;font-size:54px;line-height:1}
  .cover-sub{left:432px;top:255px;font-size:19px;font-weight:600}
  .brand{right:28px;top:26px;display:flex;align-items:center;gap:8px}
  .brand-dot{width:44px;height:44px;border-radius:50%;background:var(--blue)}
  .brand-name{font-weight:700;font-size:24px;color:var(--blue);line-height:1}
  /* toc pills */
  .toc-list{left:288px;top:68px;width:420px}
  .toc-item{height:30px;margin-bottom:15px;border-radius:15px;background:var(--pill);display:flex;align-items:center;justify-content:space-between;padding:0 0 0 18px;font-size:11px;font-weight:700;font-style:italic;color:var(--navy)}
  .toc-num{width:26px;height:26px;border-radius:50%;background:var(--green);color:#fff;font-size:10px;font-style:normal;display:flex;align-items:center;justify-content:center;margin-right:-34px}
  .toc-row{display:flex;align-items:center;gap:18px;margin-bottom:26px}
  .num-dot{width:48px;height:48px;border-radius:50%;background:var(--green);color:#fff;font-size:20px;display:flex;align-items:center;justify-content:center}
  .row-head{color:var(--sky);font-size:20px;font-weight:500;line-height:1.1}
  .row-sub{font-size:13px}
  /* cards */
  .card{background:var(--blue);border-radius:28px;color:#fff;text-align:center}
  .icon-dot{width:78px;height:78px;border-radius:50%;background:var(--green);border:4px solid #fff;display:flex;align-items:center;justify-content:center}
  .info-pill{position:absolute;left:371px;width:397px;height:117px;border-radius:36px;background:var(--blue);color:#fff;padding:20px 24px 0 54px}
  .info-pill h4,.panel h4{font-size:17px;font-weight:600}
  .info-pill p,.panel p{font-size:11.5px;line-height:1.4;color:#cfeafb}
  .step-dot{position:absolute;left:320px;width:88px;height:88px;border-radius:50%;background:var(--green);border:5px solid #fff;display:flex;align-items:center;justify-content:center}
  .caption-head{color:var(--sky);font-weight:500;font-size:16px}
</style>
</head>
<body>

<!-- Slide 1 : cover -->
<div class="frame" style="--s:.295;left:79px;top:195px">
  <section class="slide cover">
    <svg class="waves" viewBox="0 0 800 450" aria-hidden="true">
      <path d="M0 0H370C330 40 300 60 240 70C140 90 70 160 0 330Z" fill="var(--sky)"/>
      <path d="M0 330C60 190 120 110 240 80C160 130 90 220 0 360Z" fill="var(--blue)"/>
      <path d="M520 450C620 360 700 350 800 360V450Z" fill="var(--teal)"/>
      <path d="M600 450C680 400 740 390 800 395V450Z" fill="var(--green)"/>
    </svg>
    <div class="photo round" role="img" aria-label="Offshore drilling rig on open sea" style="left:50px;top:75px;width:310px;height:310px;background:radial-gradient(circle at 50% 40%,#4fb3d6,#1479a8 70%,#0d5f86)"></div>
    <div class="abs brand"><span class="brand-dot"></span><span class="brand-name">KESTREL</span></div>
    <h1 class="abs title cover-title">Oil &amp; Gas<br>Industry</h1>
    <p class="abs cover-sub">PRESENTATION TEMPLATE</p>
  </section>
</div>

<!-- Slide 2 : table of content list -->
<div class="frame raised" style="--s:.259;left:362px;top:203px">
  <section class="slide">
    <div class="photo" role="img" aria-label="Faint refinery towers background" style="left:0;top:40px;width:300px;height:410px;background:linear-gradient(180deg,#eef1f4,#f8f9fa)"></div>
    <svg class="waves" viewBox="0 0 800 450" aria-hidden="true">
      <path d="M0 0H200C150 20 90 40 0 70Z" fill="var(--royal)"/>
      <path d="M0 110C70 80 120 40 160 20C200 0 240 0 290 0C220 20 170 70 110 100C70 120 30 125 0 130Z" fill="var(--green)"/>
      <path d="M235 450C300 390 380 360 460 360C560 360 680 400 800 450Z" fill="var(--royal)"/>
    </svg>
    <h2 class="abs title" style="left:45px;top:262px;font-size:38px;color:var(--navy)">Table of<br>Content</h2>
    <div class="abs toc-list">
      <div class="toc-item">About the Company<span class="toc-num">01</span></div>
      <div class="toc-item">Challenges and Opportunities in the Energy Industry<span class="toc-num">02</span></div>
      <div class="toc-item">Our Solution<span class="toc-num">03</span></div>
      <div class="toc-item">Our Products and Services<span class="toc-num">04</span></div>
      <div class="toc-item">The Added Value We Offer<span class="toc-num">05</span></div>
      <div class="toc-item">Building the Future of Energy Together<span class="toc-num">06</span></div>
    </div>
  </section>
</div>

<!-- Slide 3 : table of content numbered -->
<div class="frame" style="--s:.294;left:615px;top:195px">
  <section class="slide">
    <svg class="waves" viewBox="0 0 800 450" aria-hidden="true">
      <path d="M480 450C620 420 720 370 800 200V450Z" fill="var(--sky)"/>
      <path d="M600 450C680 410 740 360 800 350V450Z" fill="var(--teal)"/>
      <path d="M680 450C730 420 770 400 800 398V450Z" fill="var(--green)"/>
    </svg>
    <h2 class="abs title" style="left:55px;top:68px;font-size:30px;font-weight:600">Table of Content</h2>
    <div class="abs" style="left:55px;top:135px">
      <div class="toc-row"><span class="num-dot">01</span><div><p class="row-head">CONTENT NAME</p><p class="row-sub">Fill in the following text fields with sentences</p></div></div>
      <div class="toc-row"><span class="num-dot">02</span><div><p class="row-head">CONTENT NAME</p><p class="row-sub">Fill in the following text fields with sentences</p></div></div>
      <div class="toc-row"><span class="num-dot">03</span><div><p class="row-head">CONTENT NAME</p><p class="row-sub">Fill in the following text fields with sentences</p></div></div>
      <div class="toc-row"><span class="num-dot">04</span><div><p class="row-head">CONTENT NAME</p><p class="row-sub">Fill in the following text fields with sentences</p></div></div>
    </div>
  </section>
</div>

<!-- Slide 4 : company overview -->
<div class="frame raised" style="--s:.259;left:897px;top:203px">
  <section class="slide">
    <svg class="waves" viewBox="0 0 800 450" aria-hidden="true">
      <path d="M0 0H400C300 30 200 50 120 70C70 80 30 90 0 100Z" fill="var(--sky)"/>
      <path d="M0 0H290C220 30 140 60 0 95Z" fill="var(--green)"/>
      <path d="M560 450C680 420 760 370 800 330V450Z" fill="var(--sky)"/>
      <path d="M680 450C730 420 770 400 800 390V450Z" fill="var(--green)"/>
    </svg>
    <h2 class="abs title" style="left:60px;top:122px;font-size:30px">Company<br>Overview</h2>
    <p class="abs body-text" style="left:60px;top:218px;width:310px">Presentation is a public speaking activity that aims to convey a message or information. The things conveyed can be in the form of ideas, ideas, programs, products, or services and are usually carried out in a discussion or forum. A good presentation must contain at least three important aspects which include opening, content and conclusion.</p>
    <div class="photo round" role="img" aria-label="Engineers at control room monitors" style="left:440px;top:70px;width:305px;height:305px;background:linear-gradient(135deg,#c9dbe8,#5b86a8 60%,#2b4f6e)"></div>
  </section>
</div>

<!-- Slide 5 : best product -->
<div class="frame" style="--s:.295;left:79px;top:358px">
  <section class="slide">
    <svg class="waves" viewBox="0 0 800 450" aria-hidden="true">
      <path d="M0 0H290C220 20 150 30 110 50C70 70 30 75 0 75Z" fill="var(--sky)"/>
      <path d="M0 0H190C140 20 90 50 50 65C30 72 10 75 0 75Z" fill="var(--green)"/>
    </svg>
    <h2 class="abs" style="left:60px;top:110px;font-size:30px;font-weight:400;color:var(--blue);line-height:1.3">OUR BEST<br>PRODUCT</h2>
    <p class="abs body-text" style="left:60px;top:210px;width:245px;font-size:13px">The things conveyed can be in the form of ideas, ideas, programs, products, or services and are usually carried out in a discussion or forum. A good presentation must contain at least three important aspects which include opening, content and conclusion.</p>
    <div class="abs card" style="left:336px;top:150px;width:208px;height:330px;padding-top:140px">
      <p style="font-size:19px">Content Name</p>
      <p style="font-size:13px;line-height:1.4;margin:14px 14px 0;color:#cfeafb">Presentation is a public speaking activity that aims to convey a message or information.</p>
    </div>
    <div class="photo" role="img" aria-label="Oil storage tanks" style="left:346px;top:22px;width:186px;height:186px;border-radius:50%;background:linear-gradient(180deg,#a9c6dc,#8c9aa6 55%,#5d6f5d)"></div>
    <div class="abs icon-dot" style="left:399px;top:190px">
      <svg width="34" height="34" viewBox="0 0 24 24" aria-hidden="true"><path d="M5 3h9v18H5z M14 8h3l2 3v7a1.5 1.5 0 0 1-3 0v-4h-2" fill="none" stroke="#fff" stroke-width="2"/><rect x="7" y="6" width="5" height="4" fill="#fff"/></svg>
    </div>
    <div class="abs card" style="left:558px;top:150px;width:208px;height:330px;padding-top:140px">
      <p style="font-size:19px">Content Name</p>
      <p style="font-size:13px;line-height:1.4;margin:14px 14px 0;color:#cfeafb">Presentation is a public speaking activity that aims to convey a message or information.</p>
    </div>
    <div class="photo" role="img" aria-label="LNG plant lit at dusk" style="left:568px;top:22px;width:186px;height:186px;border-radius:50%;background:linear-gradient(180deg,#c9a7d8,#4a5b8f 50%,#d9a23c 80%,#3b6f9c)"></div>
    <div class="abs icon-dot" style="left:621px;top:190px">
      <svg width="34" height="34" viewBox="0 0 24 24" aria-hidden="true"><path d="M12 2c1 4 6 6 6 12a6 6 0 0 1-12 0c0-3 2-5 3-6 0 3 2 4 2 4 0-4 0-7 1-10z" fill="none" stroke="#fff" stroke-width="2"/></svg>
    </div>
  </section>
</div>

<!-- Slide 6 : why choose us -->
<div class="frame raised" style="--s:.259;left:362px;top:365px">
  <section class="slide">
    <svg class="waves" viewBox="0 0 800 450" aria-hidden="true">
      <path d="M640 450C700 420 760 380 800 350V450Z" fill="var(--sky)"/>
      <path d="M710 450C750 430 780 415 800 410V450Z" fill="var(--green)"/>
    </svg>
    <h2 class="abs title" style="left:42px;top:52px;font-size:27px;font-weight:600">Why should<br>you choose us ?</h2>
    <div class="photo" role="img" aria-label="Yellow offshore production platform under blue sky" style="left:42px;top:160px;width:555px;height:235px;border-radius:0 0 40px 22px;border:3px solid var(--blue);background:linear-gradient(180deg,#5aa6dd,#a8d2ee 55%,#d9b64a 70%,#3c7db0)"></div>
    <div class="abs panel" style="left:342px;top:0;width:428px;height:308px;background:var(--blue);border-radius:0 0 30px 30px;padding:40px 30px 0 28px;color:#fff">
      <h4>Content Name</h4><p>Presentation is a public speaking activity that<br>aims to convey a message or information.</p>
      <h4 style="margin-top:24px">Content Name</h4><p>Presentation is a public speaking activity that<br>aims to convey a message or information.</p>
      <h4 style="margin-top:24px">Content Name</h4><p>Presentation is a public speaking activity that<br>aims to convey a message or information.</p>
    </div>
  </section>
</div>

<!-- Slide 7 : solutions -->
<div class="frame raised" style="--s:.26;left:630px;top:365px">
  <section class="slide">
    <svg class="waves" viewBox="0 0 800 450" aria-hidden="true">
      <path d="M660 0H800V160C760 120 740 60 660 0Z" fill="var(--teal)"/>
      <path d="M700 0H800V150C780 100 760 40 700 0Z" fill="var(--green)"/>
      <path d="M0 300C40 380 120 420 220 450H0Z" fill="var(--sky)"/>
      <path d="M0 360C20 410 60 440 100 450H0Z" fill="var(--blue)"/>
    </svg>
    <div class="photo round" role="img" aria-label="Field engineer in hard hat holding a tablet" style="left:50px;top:70px;width:310px;height:310px;background:linear-gradient(135deg,#4f7fb0,#9fc3dd 50%,#c8d85a 80%,#2f5c86)"></div>
    <h2 class="abs title" style="left:400px;top:100px;font-size:29px;font-weight:600">Solutions for<br>a bright future</h2>
    <p class="abs body-text" style="left:400px;top:198px;width:310px">Presentation is a public speaking activity that aims to convey a message or information. The things conveyed can be in the form of ideas, ideas, programs, products, or services and are usually carried out in a discussion or forum. A good presentation must contain at least three important aspects which include opening, content and conclusion.</p>
  </section>
</div>

<!-- Slide 8 : production steps -->
<div class="frame raised" style="--s:.261;left:898px;top:365px">
  <section class="slide">
    <svg class="waves" viewBox="0 0 800 450" aria-hidden="true">
      <path d="M0 0H340C280 30 200 40 130 55C80 65 30 70 0 75Z" fill="var(--sky)"/>
      <path d="M0 0H220C160 30 90 55 0 70Z" fill="var(--green)"/>
    </svg>
    <h2 class="abs title" style="left:45px;top:118px;font-size:29px;font-weight:600">Production<br>Steps</h2>
    <p class="abs body-text" style="left:45px;top:208px;width:250px">Presentation is a public speaking activity that aims to convey a message or information. The things conveyed can be in the form of ideas, ideas, programs, products, or services and are usually carried out in a discussion or forum.</p>
    <div class="info-pill" style="top:34px"><h4>Content Name</h4><p>Presentation is a public speaking activity that<br>aims to convey a message or information.</p></div>
    <div class="info-pill" style="top:167px"><h4>Content Name</h4><p>Presentation is a public speaking activity that<br>aims to convey a message or information.</p></div>
    <div class="info-pill" style="top:300px"><h4>Content Name</h4><p>Presentation is a public speaking activity that<br>aims to convey a message or information.</p></div>
    <div class="step-dot" style="top:48px"><svg width="40" height="40" viewBox="0 0 24 24" aria-hidden="true"><path d="M12 3 7 21M12 3l5 18M8.5 15h7M10 9h4M4 21h16" fill="none" stroke="#fff" stroke-width="2"/></svg></div>
    <div class="step-dot" style="top:181px"><svg width="40" height="40" viewBox="0 0 24 24" aria-hidden="true"><rect x="4" y="10" width="16" height="10" fill="none" stroke="#fff" stroke-width="2"/><path d="M7 10V5h4v5M14 14h3" stroke="#fff" stroke-width="2" fill="none"/></svg></div>
    <div class="step-dot" style="top:314px"><svg width="40" height="40" viewBox="0 0 24 24" aria-hidden="true"><rect x="3" y="8" width="13" height="9" fill="none" stroke="#fff" stroke-width="2"/><path d="M16 11h3l2 3v3h-5" fill="none" stroke="#fff" stroke-width="2"/><circle cx="7" cy="19" r="1.8" fill="#fff"/><circle cx="17" cy="19" r="1.8" fill="#fff"/></svg></div>
  </section>
</div>

<!-- Slide 9 : revenue chart -->
<div class="frame raised" style="--s:.26;left:94px;top:528px">
  <section class="slide">
    <div class="abs" style="left:33px;top:0;width:218px;height:275px;background:var(--blue);border-radius:0 0 28px 28px"></div>
    <h2 class="abs title white" style="left:60px;top:165px;font-size:27px;font-weight:600;line-height:1.45">Oil &amp; Gas<br>Revenue</h2>
    <svg class="abs" style="left:270px;top:20px" width="510" height="260" viewBox="0 0 510 260" aria-label="Line chart of revenue across five items">
      <g font-family="Poppins, sans-serif" font-size="12" fill="#333">
        <g stroke="#d9d9d9" stroke-width="1">
          <line x1="35" y1="20" x2="500" y2="20"/><line x1="35" y1="60" x2="500" y2="60"/><line x1="35" y1="100" x2="500" y2="100"/>
          <line x1="35" y1="140" x2="500" y2="140"/><line x1="35" y1="180" x2="500" y2="180"/><line x1="35" y1="220" x2="500" y2="220" stroke="#999"/>
        </g>
        <text x="12" y="24">50</text><text x="12" y="64">40</text><text x="12" y="104">30</text><text x="12" y="144">20</text><text x="12" y="184">10</text><text x="18" y="224">0</text>
        <text x="60" y="240">Item 1</text><text x="145" y="240">Item 2</text><text x="232" y="240">Item 3</text><text x="318" y="240">Item 4</text><text x="404" y="240">Item 5</text>
        <polyline points="80,148 166,100 252,116 338,60 424,52" fill="none" stroke="#2457d6" stroke-width="2"/>
        <polyline points="80,220 166,172 252,68 338,100 424,92" fill="none" stroke="var(--green)" stroke-width="2"/>
        <polyline points="80,172 166,204 252,140 338,160 424,20" fill="none" stroke="var(--blue)" stroke-width="2"/>
      </g>
    </svg>
    <p class="abs body-text" style="left:43px;top:295px;width:190px">The things conveyed can be in the form of ideas, ideas, programs, products, or services and are usually carried out in a discussion or forum.</p>
    <div class="abs" style="left:300px;top:290px;width:190px"><p class="caption-head">CONTENT NAME</p><p class="body-text" style="margin-top:6px">Presentation is a public speaking activity that aims to convey a message or information.</p></div>
    <div class="abs" style="left:530px;top:290px;width:190px"><p class="caption-head">CONTENT NAME</p><p class="body-text" style="margin-top:6px">Presentation is a public speaking activity that aims to convey a message or information.</p></div>
  </section>
</div>

<!-- Slide 10 : contact -->
<div class="frame raised" style="--s:.26;left:896px;top:528px">
  <section class="slide">
    <svg class="waves" viewBox="0 0 800 450" aria-hidden="true">
      <path d="M0 0H220C150 20 80 30 0 50Z" fill="var(--sky)"/>
      <path d="M0 0H110C70 20 30 35 0 45Z" fill="var(--green)"/>
      <path d="M0 390C60 400 140 420 220 450H0Z" fill="var(--sky)"/>
      <path d="M0 400C40 410 80 430 110 450H0Z" fill="var(--green)"/>
    </svg>
    <h2 class="abs title" style="left:30px;top:330px;font-size:24px;font-weight:600;transform:rotate(-90deg);transform-origin:0 0;white-space:nowrap;line-height:1.3">Get more<br>information</h2>
    <div class="photo" role="img" aria-label="Offshore gas platform with flare stack at sea" style="left:130px;top:30px;width:634px;height:252px;border-radius:30px;border:3px solid var(--blue);background:linear-gradient(180deg,#3f8fd1,#9fcbea 50%,#d7b447 65%,#2f6fa8)"></div>
    <div class="abs" style="left:130px;top:298px;width:634px;height:104px;border-radius:34px;background:var(--blue);display:flex;justify-content:space-around;align-items:center;color:#fff;font-size:13px;text-align:center">
      <div><svg width="28" height="28" viewBox="0 0 24 24" aria-hidden="true"><path d="M6 3l3 4-2 2a12 12 0 0 0 8 8l2-2 4 3-2 3C10 21 3 14 3 5z" fill="var(--green)"/></svg><p>+000-555-0142</p></div>
      <div><svg width="28" height="28" viewBox="0 0 24 24" aria-hidden="true"><circle cx="12" cy="12" r="9" fill="none" stroke="var(--green)" stroke-width="2"/><path d="M3 12h18M12 3c-4 5-4 13 0 18M12 3c4 5 4 13 0 18" fill="none" stroke="var(--green)" stroke-width="2"/></svg><p>www.kestrelenergy.example</p></div>
      <div><svg width="28" height="28" viewBox="0 0 24 24" aria-hidden="true"><circle cx="12" cy="12" r="10" fill="var(--green)"/><path d="M12 6a3.5 3.5 0 0 0-3.5 3.5C8.5 12 12 17 12 17s3.5-5 3.5-7.5A3.5 3.5 0 0 0 12 6z" fill="#fff"/></svg><p>45 Harbour Rd., Port City</p></div>
    </div>
  </section>
</div>

</body>
</html>
```